"Tarvel Mouthguards " Custom-made Mouthguard Business Website

We need an informational website for our mouthguard Business "Tarvel Mouthguards". The logo is navy blue/lime green so want to have colour scheme that goes nicely with this - have uploaded our mouthguard flyer with some information we need to put into the website but I do have more information to put in there.

Target Market(s)

Sports clubs, sportspeople, parents and kids, schools

Industry/Entity Type

Dental, Custom-made Sports Mouthguards

Coding

Number of Pages Required

5+ page

Font styles to use
Serif
Sans Serif

Colors
0054AA
0677BA
7BADD7
CADEEF
E8F1F8
0094D4
00A9DD
6FCCEA
C7EBF8
E9F6FB
00AB8E
00BBA5
67D7C9
C6EFE9
E9F9F6
59FF00
82FF00
B8FF75
E3FFCB
F4FFEA
FFF300
FFF600
FEFA6F
FFFEC7
FFFEE8
FFC000
F8CF3A
FAE287
FDF2CF
FEFAEE
F0912C
F2A743
F7CA91
FBE8D2
FDF5EE
EE7325
F08F49
F5BC92
FAE3D3
FDF4ED

Requirements
Must have
• I want drop down pages, not one scrolling page. Different pages for each heading . Content uploaded - We need a general home page with lots of pictures and info that I'll provide. A page each dedicated to 1) About Us 2) Why choose a custom mouthguard? 3) Gallery 4) Contact Us. Will need logos from "Morvex"
Nice to have
• Mainly use greens and blues, but happy to pop in some yellow/oranges/red oranges if it looks good

```html
<!DOCTYPE html>
<html lang="en">
<head>
<meta charset="utf-8">
<title>Tarvel Mouthguards – Website Pages</title>
<link href="https://fonts.googleapis.com/css2?family=Arimo:wght@400;700&display=swap" rel="stylesheet">
<style>
:root{
  --navy:#0054AA;
  --blue:#0094D4;
  --sky:#00A9DD;
  --teal:#00AB8E;
  --teal-2:#00BBA5;
  --orange:#EE7325;
  --ice:#C7EBF8;
  --mist:#E9F6FB;
  --ink:#1d2a44;
  --line:#c9c9c9;
  --grad:linear-gradient(100deg,var(--teal) 0%,var(--sky) 100%);
}
*{box-sizing:border-box;margin:0;padding:0}
html,body{width:1200px;height:4258px;overflow:hidden;background:#fff}
body{position:relative;font-family:"Arimo",Arial,sans-serif;color:var(--ink)}
.page{position:absolute;left:57px;width:533px;border:1px solid var(--line);background:#fff;overflow:hidden}
.site-head{height:58px;display:flex;align-items:center;padding:0 18px;gap:14px;font-size:5.5px;line-height:1.4;color:var(--ink)}
.partner-name{font-size:7px;font-weight:700;color:var(--navy);width:80px;border-right:1px solid var(--line);padding-right:8px;line-height:1.3}
.head-contact{width:95px}
.head-contact span{color:var(--teal)}
.brand{margin-left:auto;font-weight:700;font-size:12px;color:var(--navy);white-space:nowrap}
.site-nav{height:30px;display:flex;gap:23px;padding-left:42px;align-items:center;font-size:6.5px;color:var(--navy);background:linear-gradient(#fff,#f1f1f1)}
.site-nav .on{color:var(--orange)}
.ph{display:block}
h2{font-size:19px;color:var(--teal);font-weight:700}
p,li{font-size:6.3px;line-height:1.45}
ul{list-style:none}
ul li::before{content:"• ";}
.btn{display:inline-block;background:var(--orange);color:#fff;font-weight:700;font-size:11px;padding:3px 11px;border-radius:10px;letter-spacing:.3px}
.abs{position:absolute}

.enquiry{position:absolute;left:755px;top:47px;width:362px;height:483px;border:1px solid var(--line);padding:38px 32px}
.enquiry h2{font-size:19px;line-height:1.2;margin-bottom:20px}
.field{font-size:10.5px;border-bottom:1px solid #aaa;height:30px}
.field.msg{border:none;height:auto}
.msg-box{height:146px;border:1px solid #aaa;border-radius:8px;margin-top:8px}
.send{margin-top:14px;height:37px;border-radius:19px;background:var(--grad);color:#fff;font-weight:700;font-size:12px;display:flex;align-items:center;justify-content:center}

.step{position:absolute;top:150px;width:104px;height:118px;border-radius:10px;background:var(--grad);color:#fff;padding:30px 8px 0;text-align:center}
.step b{position:absolute;top:-9px;left:40px;width:24px;height:24px;border-radius:50%;background:var(--orange);font-size:6px;display:flex;align-items:center;justify-content:center;line-height:1.1}
.step p{font-size:5.8px}
.faq{position:absolute;left:37px;width:460px;height:55px;border-radius:7px;background:var(--grad);color:#fff;padding:10px 16px}
.faq h3{font-size:12px;margin-bottom:4px}
.faq p{font-size:5.6px}
.gallery{position:absolute;left:37px;top:102px;width:460px;height:600px;display:grid;grid-template-columns:66px 170px 88px 112px;grid-template-rows:repeat(4,1fr);gap:5px 6px}
</style>
</head>
<body>

<form class="enquiry">
  <h2>Request an<br>appointment</h2>
  <div class="field">Full name</div>
  <div class="field" style="margin-top:12px">Your email</div>
  <div class="field" style="margin-top:12px">Phone</div>
  <div class="field msg" style="margin-top:12px">Your Message<div class="msg-box"></div></div>
  <div class="send">SEND ENQUIRY</div>
</form>

<!-- Home -->
<section class="page" style="top:47px;height:320px">
  <header class="site-head"><div class="partner-name">Westbay Denture Studio</div><div class="head-contact"><span>●</span> Tarvel Mouthguards at Westbay Denture Studio<br><span>●</span> (08) 6100 2730</div><div class="head-contact"><span>●</span> info@tarvelmouthguards.com.au<br><span>●</span> Unit 7, 14 Harbour Lane, Bayside, WA 6000</div><div class="brand">Tarvel Mouthguards</div></header>
  <div style="position:absolute;top:58px;left:0;right:0;bottom:0;background:linear-gradient(100deg,var(--sky),var(--teal))">
    <nav class="site-nav" style="background:none;color:#fff"><span>Why choose us</span><span>About us</span><span>Our mouthguards</span><span>The process</span><span>Photo gallery</span><span>FAQ</span><span>Contact/bookings</span></nav>
    <div class="ph abs" role="img" aria-label="Two kids in sports uniforms holding a football and smiling with mouthguards" style="left:43px;top:43px;width:247px;height:178px;border-radius:20px;background:linear-gradient(135deg,#4f7d3e,#3c4fa8 60%,#b7a35a)"></div>
    <div class="abs" style="left:315px;top:80px;color:#fff;font-weight:700;font-size:16.5px;line-height:1.3">Protect your smile<br>with a comfortable,<br>professional fit.</div>
    <span class="btn abs" style="left:315px;top:157px">BOOK NOW</span>
  </div>
</section>

<!-- Why choose us -->
<section class="page" style="top:410px;height:318px">
  <header class="site-head"><div class="partner-name">Westbay Denture Studio</div><div class="head-contact"><span>●</span> Tarvel Mouthguards at Westbay Denture Studio<br><span>●</span> (08) 6100 2730</div><div class="head-contact"><span>●</span> info@tarvelmouthguards.com.au<br><span>●</span> Unit 7, 14 Harbour Lane, Bayside, WA 6000</div><div class="brand">Tarvel Mouthguards</div></header>
  <nav class="site-nav"><span class="on">Why choose us</span><span>About us</span><span>Our mouthguards</span><span>The process</span><span>Photo gallery</span><span>FAQ</span><span>Contact/bookings</span></nav>
  <div class="abs" style="left:62px;top:145px;width:200px">
    <h2 style="margin-bottom:8px">Why Choose Us</h2>
    <ul><li>Professionally made by a qualified dental prosthetist</li><li>Custom fit for comfort, protection, and durability</li><li>Wide range of colours and designs</li><li>Available for kids, teens, and adults</li><li><b style="color:var(--navy)">Clinic and mobile school/club visits available</b></li></ul>
  </div>
  <div class="abs" style="left:282px;top:143px;width:196px;height:92px;border-radius:12px;background:var(--grad);color:#fff;font-weight:700;font-size:11px;text-align:center;display:flex;align-items:center;justify-content:center;padding:0 14px;line-height:1.3">Talk to us about our “gap free” mouthguards for eligible private health insurance members.</div>
</section>

<!-- About us -->
<section class="page" style="top:770px;height:468px">
  <header class="site-head"><div class="partner-name">Westbay Denture Studio</div><div class="head-contact"><span>●</span> Tarvel Mouthguards at Westbay Denture Studio<br><span>●</span> (08) 6100 2730</div><div class="head-contact"><span>●</span> info@tarvelmouthguards.com.au<br><span>●</span> Unit 7, 14 Harbour Lane, Bayside, WA 6000</div><div class="brand">Tarvel Mouthguards</div></header>
  <nav class="site-nav"><span>Why choose us</span><span class="on">About us</span><span>Our mouthguards</span><span>The process</span><span>Photo gallery</span><span>FAQ</span><span>Contact/bookings</span></nav>
  <div class="ph abs" role="img" aria-label="Portrait of the dental prosthetist" style="left:42px;top:148px;width:167px;height:167px;border-radius:50%;background:var(--ice)"></div>
  <h2 class="abs" style="left:250px;top:107px">About Us</h2>
  <div class="abs" style="left:240px;top:137px;width:268px;height:312px;border-radius:12px;background:var(--grad);color:#fff;padding:12px 12px">
    <p>My name is Lena, and I am a dental prosthetist with over 20 years of experience in the dental field. I hold a Diploma of Dental Technology and an Advanced Diploma of Dental Prosthetics, which I obtained at Coastal Institute of Technology in 2011. At Tarvel Mouthguards (inside Westbay Denture Studio), my work involves designing and making custom-fitted sports mouthguards for athletes of all ages.</p>
    <p style="margin-top:4px">The goal is simple: provide mouthguards that fit well, feel comfortable, and offer reliable protection on the field, court, or in the ring. Every mouthguard is made individually, with close attention to detail, so that players can focus on their performance rather than worrying about their smile.</p>
    <p style="margin-top:4px"><b>I am committed to:</b></p>
    <ul><li>Providing safe, professional, and ethical care.</li><li>Ensuring players and parents understand their options.</li><li>Creating mouthguards that balance comfort, durability, and protection.</li><li>Maintaining up-to-date knowledge and skills through ongoing professional development.</li></ul>
    <p style="margin-top:4px">In addition to appointments at the clinic, I also provide mobile services for schools and sporting clubs, making it easier for teams to be fitted together.</p>
    <p style="margin-top:4px">Whether it's for school sport, weekend competition, or high-contact athletics, my focus is on helping athletes stay protected with mouthguards that fit with precision.</p>
    <div role="img" aria-label="Handwritten signature" style="width:90px;height:14px;margin-top:10px;border-bottom:1px solid rgba(255,255,255,.6)"></div>
    <p style="margin-top:6px">AdvDipDT, DipDT</p>
  </div>
</section>

<!-- Our mouthguards -->
<section class="page" style="top:1280px;height:723px">
  <header class="site-head"><div class="partner-name">Westbay Denture Studio</div><div class="head-contact"><span>●</span> Tarvel Mouthguards at Westbay Denture Studio<br><span>●</span> (08) 6100 2730</div><div class="head-contact"><span>●</span> info@tarvelmouthguards.com.au<br><span>●</span> Unit 7, 14 Harbour Lane, Bayside, WA 6000</div><div class="brand">Tarvel Mouthguards</div></header>
  <nav class="site-nav"><span>Why choose us</span><span>About us</span><span class="on">Our mouthguards</span><span>The process</span><span>Photo gallery</span><span>FAQ</span><span>Contact/bookings</span></nav>
  <div class="abs" style="left:42px;top:128px;width:228px">
    <h2>Our Mouthguards</h2>
    <div style="color:var(--orange);font-size:11px;margin:2px 0 10px">Protection, Comfort, Confidence</div>
    <p>Not all mouthguards are created equal. Chemist-bought “boil and bite” guards might seem convenient, but they often provide poor fit and limited protection. A custom mouthguard, professionally fitted to your teeth and bite, offers:</p>
    <ul><li>Maximum Protection – absorbs impact and helps prevent broken teeth, jaw injuries, and concussions.</li><li>Superior Comfort – designed to fit snugly, making it easier to breathe and talk while playing.</li><li>Durability – crafted from high-quality dental materials that outlast off-the-shelf options.</li></ul>
    <p style="margin-top:4px">With over 20 years experience in the industry, our dental prosthetist takes care to provide mouthguards that are made with precision and shaped for your comfort and protection.</p>
  </div>
  <div class="ph abs" role="img" aria-label="Colourful custom mouthguards and cases" style="left:285px;top:160px;width:210px;height:100px;border-radius:50px;background:linear-gradient(100deg,#d84a4a,#e9e6f5 45%,#5aa8e0 80%,#b65fc8)"></div>
  <div class="ph abs" role="img" aria-label="Rows of mouthguards in many colours and patterns" style="left:45px;top:358px;width:218px;height:125px;background:linear-gradient(180deg,#9fd07a,#b98ad8 35%,#f0a04a 65%,#6e7ee0)"></div>
  <div class="abs" style="left:292px;top:372px;width:200px">
    <div style="color:var(--teal);font-weight:700;font-size:13px;margin-bottom:8px">Types Available:</div>
    <ul><li>Kid's mouthguards – protective and comfortable for growing dentition</li><li>Single-layer: suitable for low-medium contact sports (children generally will have a single-layer mouthguard)</li><li>Double-layer: recommended for high-impact sports</li><li>Triple-layer: We are able to do triple layer mouthguards for sports that require that little bit of extra protection.</li></ul>
  </div>
  <div class="abs" style="left:42px;top:540px;width:220px">
    <div style="color:var(--teal);font-weight:700;font-size:13px;margin-bottom:10px">Design Options:</div>
    <p>Design your own mouthguard with a choice of nearly 40 colours which you can mix and match into different styles. Choose from team colours, stripes, marbled effects – even harlequin patterns. We can also offer glitter over any colour you choose.</p>
    <p style="margin-top:4px">All of our mouthguard colours and styles are locally made, right here in WA. Take a look at the full range of colours and styles you can choose from at –</p>
    <p><b>www.colourguardsupply.com</b></p>
    <p style="margin-top:4px">If you have your colours and a style in mind before your appointment with us you are one step ahead!</p>
  </div>
  <div class="ph abs" role="img" aria-label="Yellow and blue team colour mouthguards" style="left:292px;top:545px;width:198px;height:115px;border-radius:55px;background:linear-gradient(120deg,#f6e11a 45%,#2a5ad0 55%)"></div>
</section>

<!-- The process -->
<section class="page" style="top:2045px;height:393px">
  <header class="site-head"><div class="partner-name">Westbay Denture Studio</div><div class="head-contact"><span>●</span> Tarvel Mouthguards at Westbay Denture Studio<br><span>●</span> (08) 6100 2730</div><div class="head-contact"><span>●</span> info@tarvelmouthguards.com.au<br><span>●</span> Unit 7, 14 Harbour Lane, Bayside, WA 6000</div><div class="brand">Tarvel Mouthguards</div></header>
  <nav class="site-nav"><span>Why choose us</span><span>About us</span><span>Our mouthguards</span><span class="on">The process</span><span>Photo gallery</span><span>FAQ</span><span>Contact/bookings</span></nav>
  <h2 class="abs" style="left:0;right:0;top:100px;text-align:center">The Process</h2>
  <div class="step" style="left:42px"><b>Step<br>1</b><p>Book an appointment or mobile visit with our dental prosthetist.</p></div>
  <div class="step" style="left:157px"><b>Step<br>2</b><p>Impressions are taken of the mouth – this appointment will generally take around 15 minutes. You then get to choose your design (if you haven't already).</p></div>
  <div class="step" style="left:272px"><b>Step<br>3</b><p>Mouthguard is made in-house in our laboratory by our prosthetist and technicians.</p></div>
  <div class="step" style="left:387px"><b>Step<br>4</b><p>Fit and collection – you may either pick up from our clinic – or for sporting clubs or schools, we can have them packed and delivered to you.</p></div>
  <p class="abs" style="left:0;right:0;top:295px;text-align:center"><b>Now you're ready for game day!</b><br>Our turnaround time is 1-2 weeks, however we may be able to accommodate<br>faster turnaround upon request. Contact us for more details.</p>
  <div class="abs" style="left:0;right:0;top:345px;text-align:center"><span class="btn">BOOK NOW</span></div>
</section>

<!-- Gallery -->
<section class="page" style="top:2473px;height:744px">
  <header class="site-head"><div class="partner-name">Westbay Denture Studio</div><div class="head-contact"><span>●</span> Tarvel Mouthguards at Westbay Denture Studio<br><span>●</span> (08) 6100 2730</div><div class="head-contact"><span>●</span> info@tarvelmouthguards.com.au<br><span>●</span> Unit 7, 14 Harbour Lane, Bayside, WA 6000</div><div class="brand">Tarvel Mouthguards</div></header>
  <nav class="site-nav"><span>Why choose us</span><span>About us</span><span>Our mouthguards</span><span>The process</span><span class="on">Photo gallery</span><span>FAQ</span><span>Contact/bookings</span></nav>
  <div class="gallery">
    <div role="img" aria-label="Mouthguard in purple case" style="background:linear-gradient(#7a5bb0,#3d6fb5)"></div>
    <div role="img" aria-label="Glitter blue mouthguard" style="grid-row:1;grid-column:2/4;background:linear-gradient(135deg,#2d5ec2,#1a2a6e 50%,#3fa0d8)"></div>
    <div role="img" aria-label="Mouthguard in purple case" style="grid-row:1;grid-column:4;background:linear-gradient(135deg,#8a4fc8,#5fc2b8)"></div>
    <div role="img" aria-label="Teal patterned mouthguard" style="background:linear-gradient(135deg,#3fb0a8,#8c5fb6)"></div>
    <div role="img" aria-label="White mouthguard on green case" style="background:linear-gradient(135deg,#2a9a3a,#e7efe8)"></div>
    <div role="img" aria-label="Red and purple mouthguards" style="grid-column:3/5;background:linear-gradient(135deg,#c03a4a,#5a5ab8)"></div>
    <div role="img" aria-label="Pink marbled mouthguard" style="grid-column:1/3;background:linear-gradient(135deg,#e45fa0,#8a5ac0)"></div>
    <div role="img" aria-label="Mouthguard in white case" style="background:linear-gradient(#f2f2f2,#b44050)"></div>
    <div role="img" aria-label="Green and purple mouthguards" style="background:linear-gradient(135deg,#6a9a4a,#5a6ab0)"></div>
    <div role="img" aria-label="Camouflage mouthguard in case" style="background:linear-gradient(135deg,#7a7a3a,#3a5a7a)"></div>
    <div role="img" aria-label="Red and clear mouthguards" style="grid-column:2/4;background:linear-gradient(135deg,#a02a2a,#e8b8c0)"></div>
    <div role="img" aria-label="Blue glitter mouthguard on pink" style="background:linear-gradient(135deg,#d040b0,#2a40c0)"></div>
  </div>
</section>

<!-- FAQ -->
<section class="page" style="top:3260px;height:452px">
  <header class="site-head"><div class="partner-name">Westbay Denture Studio</div><div class="head-contact"><span>●</span> Tarvel Mouthguards at Westbay Denture Studio<br><span>●</span> (08) 6100 2730</div><div class="head-contact"><span>●</span> info@tarvelmouthguards.com.au<br><span>●</span> Unit 7, 14 Harbour Lane, Bayside, WA 6000</div><div class="brand">Tarvel Mouthguards</div></header>
  <nav class="site-nav"><span>Why choose us</span><span>About us</span><span>Our mouthguards</span><span>The process</span><span>Photo gallery</span><span class="on">FAQ</span><span>Contact/bookings</span></nav>
  <h2 class="abs" style="left:0;right:0;top:100px;text-align:center">FAQ</h2>
  <div class="faq" style="top:137px"><h3>How long does a mouthguard last?</h3><p>1–2 years for adults. Children generally will need a new fitting each year as their teeth and<br>size of their mouths are changing month to month.</p></div>
  <div class="faq" style="top:202px"><h3>Are mouthguards covered by health funds?</h3><p>Yes they are! Please check your coverage to ensure your policy is covered. We are pleased to offer “gap free”<br>mouthguards to private health members with dental coverage. <b>Contact us for more details.*</b></p></div>
  <div class="faq" style="top:267px"><h3>Why not buy a mouthguard from the Chemist?</h3><p>Chemist-bought “boil and bite” guards might seem convenient, but they often provide poor fit and limited protection.<br>A custom guard is just that – custom made for your mouth, providing precision fit and comfort.</p></div>
  <div class="faq" style="top:332px"><h3>Do you visit schools and clubs?</h3><p>Yes, we provide mobile fitting sessions for schools and sporting clubs.<br>Please contact us for more information or to book.</p></div>
  <p class="abs" style="left:55px;top:398px;font-size:5.8px">*Single and double layer mouthguards will be covered fully by private health insurance providing<br>your policy has mouthguard cover. Triple layer mouthguards will incur a gap payment.</p>
</section>

<!-- Contact / bookings -->
<section class="page" style="top:3753px;height:410px">
  <header class="site-head"><div class="partner-name">Westbay Denture Studio</div><div class="head-contact"><span>●</span> Tarvel Mouthguards at Westbay Denture Studio<br><span>●</span> (08) 6100 2730</div><div class="head-contact"><span>●</span> info@tarvelmouthguards.com.au<br><span>●</span> Unit 7, 14 Harbour Lane, Bayside, WA 6000</div><div class="brand">Tarvel Mouthguards</div></header>
  <nav class="site-nav"><span>Why choose us</span><span>About us</span><span>Our mouthguards</span><span>The process</span><span>Photo gallery</span><span>FAQ</span><span class="on">Contact/bookings</span></nav>
  <div class="abs" style="left:42px;top:140px;font-weight:700;font-size:18px;color:var(--navy);white-space:nowrap">Tarvel Mouthguards</div>
  <h2 class="abs" style="left:42px;top:180px">Contact / Bookings</h2>
  <div class="abs" style="left:42px;top:212px;width:170px">
    <p><b>Please contact us to make a booking<br>for your new custom mouthguard.</b></p>
    <p style="margin-top:8px"><span style="color:var(--teal)">●</span> Tarvel Mouthguards at Westbay Denture Studio</p>
    <p style="margin-top:6px"><svg width="7" height="7" viewBox="0 0 10 10"><path d="M2 1l2 2-1 1.5c.8 1.5 1.5 2.2 3 3L7.5 6l2 2-1.5 1.5C4 9 1 6 .5 2.5z" fill="#00AB8E"/></svg> (08) 6100 2730</p>
    <p style="margin-top:6px"><svg width="7" height="7" viewBox="0 0 10 10"><rect x=".5" y="2" width="9" height="6" fill="none" stroke="#00AB8E"/><path d="M.5 2l4.5 3.5L9.5 2" fill="none" stroke="#00AB8E"/></svg> info@tarvelmouthguards.com.au</p>
    <p style="margin-top:6px"><svg width="7" height="8" viewBox="0 0 10 12"><path d="M5 11S1 6.5 1 4a4 4 0 018 0c0 2.5-4 7-4 7z" fill="none" stroke="#00AB8E"/><circle cx="5" cy="4" r="1.3" fill="#00AB8E"/></svg> Unit 7, 14 Harbour Lane, Bayside,<br>&nbsp;&nbsp;&nbsp;Western Australia, 6000</p>
  </div>
  <div class="abs" style="left:42px;top:335px"><span class="btn">BOOK ONLINE NOW</span></div>
  <div class="ph abs" role="img" aria-label="Close-up of holographic glitter mouthguards" style="left:230px;top:140px;width:320px;height:220px;border-radius:50%;background:linear-gradient(120deg,#2a2a3a,#7a8ac0 35%,#c0a0d0 55%,#3a5a8a 80%,#d8d8e8)"></div>
</section>

</body>
</html>
```